Holiday Rental Company Flyer Design (DL not A5)

Note from PixelFolk Administration: The category sizing selected is A5, however the project requires DL sized artwork. Please refer to the DL template link below while the 'Special Requirements' are updated accordingly.

Project Brief:
We need a double sided DL flyer designed for an up market Holiday Rental Company that portrays a personalised approach to property management. These are to be used for letter box drops to homes we're specifically targeting so the design should be modern, complimentary colour palette, uncluttered & visually appealing.

Please Download the DL Template from Quillmark here: http://www.quillmark.com.au/qm/ns/propath/UploadResources.aspx?selectedTab=0?pfid=BFB&pf_id=BFB&xnav=easypath-upload-image#Templates

Target Market(s)

Wealthy Home Owners

Industry/Entity Type

It Company

Font styles to use
Other font styles liked:
• Avant Garde Extra Light & Demi

Colors
33b8a4

Requirements
Must have
• DL Flyer sizes (210mm width x 99mm width, plus 3mm bleed)
• Front: Logo, Main Image & Grab
• Back: Contact Details & Brief Description of our business
• Images: Ideally the main image should be the house with the pool but alternatively a lifestyle images could also be used.
Nice to have
• A creative designer!
Should not have
• Clutter & busy designs

```html
<!DOCTYPE html>
<html lang="en">
<head>
<meta charset="utf-8">
<title>Harbourline Stays – DL Flyer</title>
<link rel="stylesheet" href="https://fonts.googleapis.com/css2?family=Didact+Gothic&family=Montserrat:wght@600;700&family=Questrial&display=swap">
<style>
  :root {
    --teal: #33b8a4;
    --teal-deep: #1fa08c;
    --slate: #6b6c70;
    --ink: #5a5a5a;
    --paper: #ffffff;
    --mist: #e2e3e5;
    --stage: #ececec;
    --night-1: #1c1e6e;
    --night-2: #4a3a9c;
    --night-3: #2f7ee0;
  }
  * { box-sizing: border-box; margin: 0; padding: 0; }
  html, body { width: 1200px; height: 800px; overflow: hidden; }
  body {
    background: var(--stage);
    font-family: "Didact Gothic", "Questrial", sans-serif;
    position: relative;
  }
  .flyer {
    position: absolute;
    left: 210px;
    width: 780px;
    height: 368px;
    overflow: hidden;
    box-shadow: 0 6px 18px rgba(0,0,0,.18);
  }
  .flyer--back { top: 24px; display: flex; background: var(--paper); }
  .flyer--front { top: 408px; }

  /* Back side */
  .story { width: 400px; display: flex; flex-direction: column; }
  .story__text {
    height: 250px;
    padding: 26px 30px 0 30px;
    background: linear-gradient(160deg, var(--paper) 30%, var(--mist) 100%);
    color: var(--ink);
    font-size: 11.5px;
    line-height: 1.45;
  }
  .story__title {
    font-family: "Montserrat", sans-serif;
    font-weight: 700;
    color: var(--teal);
    font-size: 24px;
    margin-bottom: 10px;
  }
  .story__text p { margin-bottom: 8px; }
  .story__text strong { font-family: "Montserrat", sans-serif; font-weight: 700; color: #333; }
  .benefits { list-style: none; color: var(--teal); }
  .benefits li { position: relative; padding-left: 12px; margin-bottom: 2px; }
  .benefits li::before { content: "•"; position: absolute; left: 0; }
  .lifestyle-row {
    flex: 1;
    background: #d9dadc;
    display: flex;
    gap: 8px;
    padding: 10px 10px 10px 30px;
  }
  .lifestyle-tile { flex: 1; }
  .lifestyle-tile--table { background: linear-gradient(135deg, #c98a4a, #7a5a44 60%, #dcd6cc); }
  .lifestyle-tile--jetty { background: linear-gradient(180deg, #cfe3ee, #8fbfd8); }
  .lifestyle-tile--swim { background: linear-gradient(135deg, #4fb9c9, #2a8ea6); }

  .contact { width: 380px; display: flex; flex-direction: column; }
  .contact__accent { height: 16px; background: var(--teal); }
  .contact__photo {
    height: 140px;
    background: linear-gradient(135deg, #e4e4e2, #b9bab8 55%, #8f908e);
  }
  .contact__cta {
    height: 106px;
    background: var(--slate);
    color: #fff;
    padding: 16px 26px;
    font-size: 12.5px;
    line-height: 1.45;
  }
  .contact__cta-strong {
    margin-top: 6px;
    font-family: "Montserrat", sans-serif;
    font-weight: 700;
    font-size: 15px;
    letter-spacing: .5px;
  }
  .contact__details {
    flex: 1;
    background: var(--teal);
    color: #fff;
    padding: 14px 26px;
    font-size: 13px;
    line-height: 1.55;
  }
  .contact__address { margin-top: 4px; }

  /* Front side */
  .hero {
    position: absolute; inset: 0;
    background:
      radial-gradient(ellipse at 18% 85%, var(--night-3) 0%, rgba(47,126,224,0) 45%),
      radial-gradient(ellipse at 70% 20%, #b58a4a 0%, rgba(181,138,74,0) 35%),
      linear-gradient(160deg, #3b2f5e 0%, var(--night-2) 45%, var(--night-1) 100%);
  }
  .brand {
    position: absolute;
    top: 34px; right: 40px;
    width: 180px; height: 112px;
    background: var(--teal);
    display: flex; flex-direction: column; justify-content: center; align-items: center;
    color: #fff;
    font-family: "Didact Gothic", sans-serif;
    font-size: 19px;
    letter-spacing: 4px;
    line-height: 1.25;
    text-align: center;
  }
  .headline {
    position: absolute;
    left: 130px; top: 196px;
    color: #fff;
    font-family: "Questrial", sans-serif;
    font-size: 32px;
    letter-spacing: 1px;
  }
  .tagline {
    position: absolute;
    left: 170px; right: 0; top: 244px;
    height: 48px;
    background: var(--teal);
    color: #fff;
    font-family: "Montserrat", sans-serif;
    font-weight: 700;
    font-size: 28px;
    line-height: 48px;
    padding-left: 80px;
  }
</style>
</head>
<body>

<section class="flyer flyer--back">
  <div class="story">
    <div class="story__text">
      <h2 class="story__title">What We Do Differently!</h2>
      <p>Rather than relying upon a key safe or a central pickup destination, a Harbourline Stays staff member will greet guests upon arrival.</p>
      <p>Our <strong>Meet &amp; Greet</strong> service provides home owners with an increased level of Security and also allows us to:</p>
      <ul class="benefits">
        <li>Prepare the home for their arrival (lights, heaters, music etc)</li>
        <li>Establish a rapport &amp; help facilitate future bookings</li>
        <li>Reiterate their responsibilities to ensure the return of their bond</li>
      </ul>
    </div>
    <div class="lifestyle-row">
      <div class="lifestyle-tile lifestyle-tile--table" role="img" aria-label="Dining table with tulips in a vase"></div>
      <div class="lifestyle-tile lifestyle-tile--jetty" role="img" aria-label="Calm bay water with a jetty"></div>
      <div class="lifestyle-tile lifestyle-tile--swim" role="img" aria-label="Dolphins swimming in clear water"></div>
    </div>
  </div>
  <div class="contact">
    <div class="contact__accent"></div>
    <div class="contact__photo" role="img" aria-label="Modern bathroom with a freestanding bath and white flowers"></div>
    <div class="contact__cta">
      <p>If you'd like to know what your property could achieve or require additional information,</p>
      <p class="contact__cta-strong">PLEASE CONTACT US ON:</p>
    </div>
    <div class="contact__details">
      <p>t. (03) 5550 0142</p>
      <p>e. stay@harbourlinestays.com.au</p>
      <p>w. harbourlinestays.com.au</p>
      <p class="contact__address">PO Box 12, Seaview Victoria 3999</p>
    </div>
  </div>
</section>

<section class="flyer flyer--front">
  <div class="hero" role="img" aria-label="Luxury house with a lit swimming pool at night"></div>
  <div class="brand"><span>HARBOURLINE</span><span>STAYS</span></div>
  <h1 class="headline">Holiday Rental Management</h1>
  <p class="tagline">with a difference</p>
</section>

</body>
</html>
```